bluefernworks.com website design

We're looking for a website design for Bluefernworks.com .
Bluefern is a manufacturer of high visibility traffic safety equipment and gear.. Our initial site will be a product catalog site featuring traffic cones . We will eventually expand to include traffic barriers, mesh signs, safety clothing and more. Our logo and product pictures can be found at bluefernworks.com .
Updates

Target Market(s)

We service a wide range of customers with our focus markets being construction, manufacturing and municipalities.

Industry/Entity Type

Safety Products

Number of Pages Required

1 page

Font styles to use
Sans Serif

Requirements
Must have
• company logo w/compatible color scheme

```html
<!DOCTYPE html>
<html lang="en">
<head>
<meta charset="utf-8">
<title>Bluefern Safety Products</title>
<link href="https://fonts.googleapis.com/css2?family=Nunito+Sans:wght@400;600;700;800;900&display=swap" rel="stylesheet">
<style>
:root{
  --orange:#e9822f;
  --ink:#222222;
  --text:#3a3a3a;
  --muted:#555555;
  --soft:#f3f2f0;
  --line:#d8d8d8;
  --footer:#141414;
  --white:#ffffff;
}
*{margin:0;padding:0;box-sizing:border-box}
html,body{width:1200px;height:2825px;overflow:hidden;background:var(--white)}
body{position:relative;font-family:"Nunito Sans",Arial,sans-serif;color:var(--text)}
.abs{position:absolute}

/* header */
.site-header{position:absolute;left:0;top:0;width:1200px;height:120px;background:var(--white)}
.brand{position:absolute;display:flex;flex-direction:column;align-items:flex-start}
.brand-row{display:flex;align-items:center;gap:10px}
.brand-dot{width:46px;height:46px;border-radius:50%;background:var(--orange)}
.brand-name{font-weight:800;color:var(--orange);font-size:34px;line-height:1}
.brand-tag{font-weight:700;color:#555;font-size:15px;margin-top:2px;padding-left:70px}
.contact-chip{position:absolute;display:flex;align-items:center;gap:10px;top:24px}
.chip-icon{width:28px;height:28px;border-radius:50%;background:var(--orange);display:flex;align-items:center;justify-content:center}
.chip-label{font-size:12px;font-weight:600;color:var(--ink)}
.chip-value{font-size:16px;font-weight:600;color:var(--ink)}
.main-nav{position:absolute;top:82px;left:531px;display:flex}
.main-nav a{font-size:14px;color:var(--ink);text-decoration:none;margin-right:32px;padding-bottom:6px}
.main-nav a.active{color:var(--orange);border-bottom:2px solid var(--orange)}

/* hero */
.hero{position:absolute;left:0;top:120px;width:1200px;height:480px;background:linear-gradient(90deg,#6f6d6b 0%,#4a4a4c 45%,#5b5d61 100%)}
.hero-panel{position:absolute;left:649px;top:109px;width:551px;height:238px;background:rgba(40,40,40,.88);border-radius:60px 0 0 60px;padding:36px 120px 0 59px}
.hero-title{font-weight:900;font-size:36px;color:var(--white);letter-spacing:.5px}
.hero-text{font-size:14px;color:var(--white);line-height:19px;margin-top:10px;text-align:justify}
.btn{display:inline-block;background:var(--orange);color:var(--white);font-weight:800;font-size:13px;border-radius:18px;padding:0 17px;height:35px;line-height:35px;letter-spacing:.3px}
.hero-panel .btn{margin-top:16px}
.dots{position:absolute;top:441px;left:568px;display:flex;gap:6px}
.dots span{width:8px;height:8px;border-radius:50%;border:1.5px solid var(--white)}
.dots span.on{background:var(--white)}

/* section titles */
.section-title{position:absolute;left:0;width:1200px;text-align:center;font-weight:800;font-size:19px;color:var(--ink)}
.section-title::after{content:"";display:block;width:38px;height:2px;background:var(--orange);margin:17px auto 0}

/* categories */
.cat-img{position:absolute;top:721px;width:223px;height:250px;border-radius:14px}
.cat-btn{position:absolute;top:988px;width:222px;height:37px;border:1px solid #444;border-radius:8px;text-align:center;line-height:35px;font-weight:800;font-size:14px;color:var(--ink)}

/* welcome */
.welcome{position:absolute;left:0;top:1087px;width:1200px;height:432px;background:var(--soft)}
.welcome-photo{position:absolute;left:546px;top:0;width:654px;height:432px;border-radius:20px 0 0 0;background:linear-gradient(160deg,#7fa45b 0%,#9aa8b3 30%,#e47a35 55%,#6c6c6c 100%)}
.welcome-heading{position:absolute;left:133px;top:66px;display:flex;align-items:center;gap:14px}
.welcome-heading h2{font-weight:800;font-size:19px;color:var(--ink)}
.welcome-heading h2 em{font-style:normal;color:var(--orange)}
.body-copy{font-size:13px;line-height:17.6px;color:var(--text)}

/* products */
.product{position:absolute;top:1652px;width:222px;height:296px;border:1px solid var(--line);border-radius:16px;text-align:center}
.product-img{width:80px;height:160px;margin:16px auto 0;border-radius:6px}
.product h3{font-weight:800;font-size:16px;color:var(--ink);margin-top:23px}
.product p{font-size:13px;line-height:18px;color:var(--muted);margin-top:14px;padding:0 28px}
.arrow{position:absolute;top:1774px;width:32px;height:32px}

/* safety */
.safety{position:absolute;left:0;top:2002px;width:1200px;height:475px;background:var(--soft)}
.safety-photo{position:absolute;left:131px;top:38px;width:564px;height:398px;border-radius:16px;background:linear-gradient(180deg,#5ea0e0 0%,#a9cdf0 40%,#d94a3f 65%,#6a9a3c 100%)}
.safety-title{position:absolute;left:761px;top:80px;font-weight:800;font-size:19px;color:var(--ink)}
.safety-title::after{content:"";display:block;width:78px;height:2px;background:var(--orange);margin-top:17px}

/* footer */
.site-footer{position:absolute;left:0;top:2477px;width:1200px;height:348px;background:var(--footer);color:var(--white)}
.foot-h{position:absolute;top:53px;font-weight:800;font-size:13px;letter-spacing:.3px}
.foot-item{position:absolute;display:flex;gap:11px;align-items:flex-start;font-size:12px;line-height:15.5px}
.foot-icon{width:24px;height:24px;border-radius:50%;background:var(--white);flex:none;display:flex;align-items:center;justify-content:center;margin-top:3px}
.foot-menu{position:absolute;left:791px;top:86px;font-size:12px;line-height:24px}
.foot-rule{position:absolute;left:131px;top:266px;width:938px;height:1px;background:#333}
.copyright{position:absolute;top:304px;left:0;width:1200px;text-align:center;font-size:11px}
</style>
</head>
<body>

<header class="site-header">
  <div class="brand" style="left:133px;top:22px">
    <div class="brand-row"><span class="brand-dot"></span><span class="brand-name">Bluefern</span></div>
    <div class="brand-tag">Safety Products</div>
  </div>
  <div class="contact-chip" style="left:620px">
    <span class="chip-icon"><svg width="12" height="9" viewBox="0 0 12 9"><rect x="0.5" y="0.5" width="11" height="8" rx="1" fill="#fff"/><path d="M1 1l5 4 5-4" stroke="#e9822f" fill="none"/></svg></span>
    <div><div class="chip-label">EMAIL US</div><div class="chip-value">info@bluefernworks.com</div></div>
  </div>
  <div class="contact-chip" style="left:900px">
    <span class="chip-icon"><svg width="12" height="12" viewBox="0 0 24 24"><path fill="#fff" d="M6.6 10.8a15.2 15.2 0 0 0 6.6 6.6l2.2-2.2a1 1 0 0 1 1-.25 11.4 11.4 0 0 0 3.6.57 1 1 0 0 1 1 1V20a1 1 0 0 1-1 1A17 17 0 0 1 3 4a1 1 0 0 1 1-1h3.5a1 1 0 0 1 1 1c0 1.25.2 2.45.57 3.57a1 1 0 0 1-.25 1z"/></svg></span>
    <div><div class="chip-label">CALL US</div><div class="chip-value">+1 555 014 2290</div></div>
  </div>
  <nav class="main-nav">
    <a class="active">HOME</a><a>ABOUT US</a><a>SERVICES</a><a>PRODUCTS</a><a>BLOG</a><a style="margin-right:0">CONTACT US</a>
  </nav>
</header>

<section class="hero" role="img" aria-label="Photo of orange and white traffic cones lined up on an asphalt road">
  <div class="hero-panel">
    <h1 class="hero-title">TRAFFIC CONES</h1>
    <p class="hero-text">There are many variations of passages of Lorem Ipsum available, but the majority have suffered alteration in some form, by injected humour</p>
    <span class="btn">READ MORE</span>
  </div>
  <div class="dots"><span class="on"></span><span class="on"></span><span></span><span></span><span class="on"></span></div>
</section>

<h2 class="section-title" style="top:644px">CATEGORIES</h2>

<div class="cat-img" style="left:131px;background:linear-gradient(160deg,#8a8a8a,#5c5c5c 55%,#e8742d)" role="img" aria-label="Photo of traffic cones on a road"></div>
<div class="cat-img" style="left:369px;background:linear-gradient(180deg,#1d7be0,#5aa9ef 60%,#c9362f)" role="img" aria-label="Photo of a red stop sign against blue sky"></div>
<div class="cat-img" style="left:607px;background:linear-gradient(135deg,#6d8a4e,#b9c1b5 50%,#e05a32)" role="img" aria-label="Photo of a row of orange traffic barrier posts"></div>
<div class="cat-img" style="left:845px;background:linear-gradient(180deg,#e9e9e9,#c8e63a 55%,#2a2a2a)" role="img" aria-label="Photo of a person wearing a high visibility safety vest"></div>
<div class="cat-btn" style="left:131px">TRAFFIC CONES</div>
<div class="cat-btn" style="left:368px">MESH SIGNS</div>
<div class="cat-btn" style="left:607px">TRAFFIC BARRIERS</div>
<div class="cat-btn" style="left:846px">SAFETY CLOTHING</div>

<section class="welcome">
  <div class="welcome-heading">
    <span class="brand-dot" style="width:40px;height:40px"></span>
    <h2>WELCOME TO <em>BLUEFERN</em></h2>
  </div>
  <p class="body-copy abs" style="left:131px;top:157px;width:355px">Sed ut perspiciatis unde omnis iste natus error sit voluptatem accusantium doloremque laudantium, totam rem aperiam, eaque ipsa quae ab illo inventore veritatis et quasi architecto beatae vitae dicta sunt explicabo. Nemo enim ipsam voluptatem quia voluptas sit aspernatur aut odit aut fugit, sed quia consequuntur magni dolores eos qui ratione voluptatem sequi nesciunt. Neque porro quisquam est, qui dolorem ipsum quia dolor sit amet, consectetur, adipisci velit, sed quia non numquam.</p>
  <span class="btn abs" style="left:131px;top:345px">READ MORE</span>
  <div class="welcome-photo" role="img" aria-label="Photo of orange and white road closed barricades across a highway"></div>
</section>

<h2 class="section-title" style="top:1566px">TRAFFIC CONES</h2>

<svg class="arrow" style="left:64px" viewBox="0 0 32 32"><circle cx="16" cy="16" r="15" fill="none" stroke="#222" stroke-width="1.4"/><path d="M18 10l-6 6 6 6" fill="none" stroke="#222" stroke-width="1.6"/></svg>
<svg class="arrow" style="left:1102px" viewBox="0 0 32 32"><circle cx="16" cy="16" r="15" fill="none" stroke="#222" stroke-width="1.4"/><path d="M14 10l6 6-6 6" fill="none" stroke="#222" stroke-width="1.6"/></svg>

<div class="product" style="left:131px"><div class="product-img" style="background:linear-gradient(180deg,#fff 0%,#f7772a 45%,#222 95%)" role="img" aria-label="Orange cone with reflective collars"></div><h3>BF-C2810R</h3><p>28" 10lb Orange Cone w/(2) Brightline Collars</p></div>
<div class="product" style="left:368px"><div class="product-img" style="background:linear-gradient(180deg,#fff 0%,#f7772a 40%,#222 98%)" role="img" aria-label="Tall orange cone with reflective collars"></div><h3>BF-C3612R</h3><p>36" 12lb Orange Cone w/(2) Brightline Collars</p></div>
<div class="product" style="left:607px"><div class="product-img" style="background:linear-gradient(180deg,#fff 0%,#ef4a1f 30%,#222 98%)" role="img" aria-label="Plain tall orange cone"></div><h3>BF-C3612P</h3><p>36" 12lb Orange Cone</p></div>
<div class="product" style="left:846px"><div class="product-img" style="background:linear-gradient(180deg,#fff 0%,#a8e61a 50%,#222 98%)" role="img" aria-label="Lime green cone with reflective collars"></div><h3>BF-L2807R</h3><p>28" 7lb Lime Cone w/(2) Brightline Collars</p></div>

<section class="safety">
  <div class="safety-photo" role="img" aria-label="Photo of red and white road barriers with warning lamps and a yellow street sign"></div>
  <h2 class="safety-title">TRAFFIC SAFETY</h2>
  <p class="body-copy abs" style="left:764px;top:148px;width:300px">Sed ut perspiciatis unde omnis iste natus error sit voluptatem accusantium doloremque laudantium, totam rem aperiam, eaque ipsa quae ab illo inventore veritatis et quasi architecto beatae vitae dicta sunt explicabo. Nemo enim ipsam voluptatem quia voluptas sit aspernatur aut odit aut fugit, sed quia consequuntur magni dolores eos qui ratione voluptatem sequi nesciunt. Neque porro quisquam est, qui dolorem ipsum quia dolor sit amet, consectetur, adipisci velit, sed quia non numquam.</p>
  <span class="btn abs" style="left:764px;top:373px">READ MORE</span>
</section>

<footer class="site-footer">
  <div class="brand" style="left:140px;top:86px">
    <div class="brand-row"><span class="brand-dot"></span><span class="brand-name">Bluefern</span></div>
    <div class="brand-tag" style="color:#888">Safety Products</div>
  </div>

  <div class="foot-h" style="left:447px">CONTACT US</div>
  <div class="foot-item" style="left:447px;top:88px">
    <span class="foot-icon"><svg width="10" height="13" viewBox="0 0 10 13"><path d="M5 0a5 5 0 0 0-5 5c0 3.5 5 8 5 8s5-4.5 5-8a5 5 0 0 0-5-5z" fill="#141414"/><circle cx="5" cy="5" r="1.8" fill="#fff"/></svg></span>
    <div>Suite 204, Level 2 West,<br>415-421 Harbour Road, Kelsey Bay 4870.</div>
  </div>
  <div class="foot-item" style="left:447px;top:139px">
    <span class="foot-icon"><svg width="11" height="11" viewBox="0 0 24 24"><path fill="#141414" d="M6.6 10.8a15.2 15.2 0 0 0 6.6 6.6l2.2-2.2a1 1 0 0 1 1-.25 11.4 11.4 0 0 0 3.6.57 1 1 0 0 1 1 1V20a1 1 0 0 1-1 1A17 17 0 0 1 3 4a1 1 0 0 1 1-1h3.5a1 1 0 0 1 1 1c0 1.25.2 2.45.57 3.57a1 1 0 0 1-.25 1z"/></svg></span>
    <div>Call Us<br>+1 555 014 2290</div>
  </div>
  <div class="foot-item" style="left:447px;top:190px">
    <span class="foot-icon"><svg width="11" height="8" viewBox="0 0 12 9"><rect x="0.5" y="0.5" width="11" height="8" rx="1" fill="#141414"/><path d="M1 1l5 4 5-4" stroke="#fff" fill="none"/></svg></span>
    <div>E mail Us<br>info@bluefernworks.com</div>
  </div>

  <div class="foot-h" style="left:791px">MENU</div>
  <div class="foot-menu">HOME<br>ABOUT US<br>SERVICES<br>PRODUCTS<br>BLOG<br>CONTACT US</div>

  <div class="foot-h" style="left:967px">FOLLOW US</div>
  <div class="foot-item" style="left:965px;top:84px"><span class="foot-icon"></span><div>Like us on<br>FRIENDSPHERE</div></div>
  <div class="foot-item" style="left:965px;top:134px"><span class="foot-icon"></span><div>Follow us on<br>CHIRPLINE</div></div>
  <div class="foot-item" style="left:965px;top:185px"><span class="foot-icon"></span><div>Follow us on<br>WORKGRAPH</div></div>

  <div class="foot-rule"></div>
  <div class="copyright">Copyright © 2023 All Rights Reserved</div>
</footer>

</body>
</html>
```